Letterhead Design Project

Our firm recently came out with a new logo and new website and we would like to design letterhead that makes use of the new look.

Our firm is an energy consulting firm. We help our customers find ways to spend less money on their energy expenses (we cater to commercial and industrial accounts) by helping them find a lower rate for every unit of energy they consume, install more energy efficient measures so that they end up using fewer units of energy or determine if making the energy themselves can be done more cost effectively

Industry/Entity Type

Industrial

Requirements
Must have
• Must have our logo
must have our contact information
Nice to have
• some sort of watermark

```html
<!DOCTYPE html>
<html lang="en">
<head>
<meta charset="utf-8">
<title>Lumivale Energy Solutions — Letterhead</title>
<link rel="stylesheet" href="https://fonts.googleapis.com/css2?family=Montserrat:wght@300;400;500&display=swap">
<style>
  :root {
    --paper: #ffffff;
    --slate: #a7a9ac;
    --teal: #2aa8c4;
    --ink: #3c3f44;
  }
  * { margin: 0; padding: 0; box-sizing: border-box; }
  html, body { width: 891px; height: 1200px; overflow: hidden; background: var(--paper); }
  .letterhead {
    position: relative;
    width: 891px;
    height: 1200px;
    background: var(--paper);
    font-family: "Montserrat", Arial, sans-serif;
  }
  .side-panel {
    position: absolute;
    left: 30px;
    top: 0;
    width: 154px;
    height: 624px;
    background: var(--slate);
  }
  .accent-bar {
    position: absolute;
    left: 30px;
    top: 428px;
    width: 27px;
    height: 434px;
    background: var(--teal);
  }
  .brand {
    position: absolute;
    left: 234px;
    top: 52px;
    display: flex;
    align-items: center;
    gap: 18px;
  }
  .brand-mark {
    width: 30px;
    height: 30px;
    background: var(--teal);
  }
  .brand-name {
    font-weight: 400;
    font-size: 44px;
    letter-spacing: 14px;
    color: var(--ink);
    line-height: 1;
  }
  .brand-tagline {
    position: absolute;
    left: 286px;
    top: 106px;
    font-weight: 400;
    font-size: 11px;
    letter-spacing: 17px;
    color: var(--ink);
  }
  .contact {
    position: absolute;
    right: 22px;
    top: 44px;
    writing-mode: vertical-rl;
    font-weight: 400;
    font-size: 17px;
    line-height: 22px;
    color: var(--teal);
  }
  .website {
    position: absolute;
    left: 0;
    width: 100%;
    top: 1096px;
    text-align: center;
    font-weight: 400;
    font-size: 14px;
    color: var(--teal);
  }
</style>
</head>
<body>
  <div class="letterhead">
    <div class="side-panel"></div>
    <div class="accent-bar"></div>

    <header class="brand">
      <span class="brand-mark"></span>
      <span class="brand-name">LUMIVALE</span>
    </header>
    <div class="brand-tagline">ENERGY SOLUTIONS</div>

    <address class="contact">
      <span>1820 Harbor Crest Dr</span><br>
      <span>Coastline, CA</span><br>
      <span>90417-3308</span><br>
      <span>(555) 014-2280</span>
    </address>

    <footer class="website">www.lumivalees.com</footer>
  </div>
</body>
</html>
```